Wren Sporting Goods Inc.

Need to create a website that is informational and has the ability to sell goods and services. Such as a custom t shirt designer where the user can upload and image to be displayed on the garmet. The sports we specialize in are basketball, football, and baseball.

Would like like:
Home Page
Locker Room Page:
Custom Uniforms Page
Custom Shirt Creator
Brands
About

Competitor websites are
tundrafieldwearnx.com
dvq.com
lumarogear.com

```html
<!DOCTYPE html>
<html lang="en">
<head>
<meta charset="utf-8">
<title>Wren Sporting Goods</title>
<link rel="stylesheet" href="https://fonts.googleapis.com/css2?family=Oswald:wght@500;600;700&family=Inter:wght@400;500;600;700&display=swap">
<style>
:root{
  --ink:#0f0f10;
  --ink-2:#18181b;
  --ink-3:#232326;
  --red:#e0262b;
  --red-dark:#b81c20;
  --blue:#2563eb;
  --navy:#3a4a9c;
  --purple:#6b4fa0;
  --light:#f4f5f7;
  --white:#ffffff;
  --muted:#9ca3af;
  --muted-dark:#6b7280;
  --text:#1f2023;
  --line:#e5e7eb;
}
*{box-sizing:border-box;margin:0;padding:0}
html,body{width:1200px;height:4354px;overflow:hidden}
body{font-family:"Inter",sans-serif;background:var(--ink);color:var(--white);font-size:11px}
.wrap{width:808px;margin:0 auto;position:relative}
.display{font-family:"Oswald",sans-serif;font-weight:600;text-transform:uppercase;letter-spacing:.2px;line-height:1.1}
.tag{display:inline-block;font-size:8.5px;font-weight:600;text-transform:uppercase;letter-spacing:.5px;color:var(--red);background:rgba(224,38,43,.12);padding:3px 8px;border-radius:20px}
.tag.blue{color:#60a5fa;background:rgba(37,99,235,.18)}
.btn{display:inline-flex;align-items:center;gap:6px;font-size:11px;font-weight:600;padding:0 20px;height:30px;border-radius:4px;color:var(--white);background:var(--red)}
.btn.blue{background:var(--blue)}
.btn.ghost{background:var(--white);color:var(--text);border:1px solid var(--line)}
.photo{border-radius:8px}

.nav{position:absolute;top:0;left:0;width:1200px;height:46px;background:rgba(15,15,16,.92);z-index:5}
.nav .wrap{display:flex;align-items:center;height:46px}
.brand{font-family:"Oswald",sans-serif;font-weight:600;font-size:17px;color:var(--white);display:flex;align-items:center;gap:7px;text-transform:uppercase}
.brand i{width:10px;height:10px;background:var(--red);display:block}
.nav ul{list-style:none;display:flex;gap:20px;margin-left:80px;font-size:10.5px;color:#d4d4d8}
.nav .cart{margin-left:auto;margin-right:16px}
.nav .btn{height:24px;padding:0 11px;font-size:10px}

.hero{height:558px;position:relative;text-align:center;
  background:radial-gradient(ellipse 380px 420px at 180px 220px,rgba(160,30,40,.55),transparent 70%),
  radial-gradient(ellipse 380px 420px at 1030px 200px,rgba(30,70,160,.55),transparent 70%),
  linear-gradient(#1a1a1d,#111113 80%,var(--ink))}
.hero-player{position:absolute;top:40px;width:330px;height:480px;opacity:.55;border-radius:50% 50% 10% 10%}
.hero-player.left{left:150px;background:linear-gradient(#4a2a2e,#2a1a1c)}
.hero-player.right{right:150px;background:linear-gradient(#2a3550,#1a1f2e)}
.hero-inner{position:relative;padding-top:120px}
.hero .tag{background:none;color:#8a2a2e;font-size:9px}
.hero h1{font-size:54px;margin-top:12px;line-height:1.1}
.hero h1 span{display:block;background:linear-gradient(90deg,#6b4fa0,#8a6cc4);-webkit-background-clip:text;background-clip:text;color:transparent}
.hero p{font-size:12.5px;color:#d4d4d8;width:400px;margin:26px auto 0;line-height:1.45}
.hero .actions{display:flex;justify-content:center;gap:14px;margin-top:30px}
.hero .actions .btn{height:34px;width:184px;justify-content:center}
.stats{display:flex;justify-content:center;gap:26px;margin-top:36px;font-size:9px;color:#a1a1aa}
.stats span{display:flex;align-items:center;gap:6px}

.built{height:380px;text-align:center;padding-top:48px}
.built h2{font-size:34px}
.built h2 em{font-style:normal;color:var(--red)}
.built > .wrap > p{font-size:11.5px;color:#d4d4d8;margin-top:14px}
.sports{display:flex;gap:20px;margin-top:38px;text-align:left}
.sport{width:256px;height:156px;border-radius:8px;background:linear-gradient(135deg,#3a3a3e,#232326);padding:20px}
.sport .ball{width:38px;height:38px;border-radius:50%}
.sport h3{font-family:"Oswald",sans-serif;font-weight:600;font-size:15px;margin-top:20px}
.sport p{font-size:9.5px;color:var(--muted);margin-top:9px;line-height:1.45}

.uniforms{height:502px;background:var(--light);color:var(--text)}
.split{display:flex;align-items:center;gap:40px;height:100%}
.split .media{width:384px;height:384px;flex:none;position:relative}
.uniforms .media{background:linear-gradient(160deg,#c8cad0,#8e3a44 55%,#2c3a78)}
.media .cap{position:absolute;left:18px;bottom:18px;font-family:"Oswald",sans-serif;font-size:9px;color:#f3d3d5;text-transform:uppercase}
.copy{flex:1}
.copy h2{font-size:34px;margin-top:12px}
.uniforms h2 span{display:block;color:#a3232b}
.copy > p{font-size:11px;line-height:1.6;color:var(--muted-dark);margin-top:14px;width:380px}
.checks{display:grid;grid-template-columns:1fr 1fr;gap:9px 0;margin-top:18px;font-size:9.5px;color:#4b5563;list-style:none}
.checks li{display:flex;align-items:center;gap:8px}
.checks svg{flex:none}
.copy .actions{display:flex;gap:10px;margin-top:22px}
.copy .actions .btn{height:26px;font-size:10px;padding:0 20px}

.creator{height:504px;background:var(--ink)}
.creator h2{font-size:34px}
.creator h2 em{font-style:normal;color:var(--blue)}
.creator .copy > p{color:#c4c4cc}
.steps{display:grid;grid-template-columns:1fr 1fr;gap:18px 20px;margin-top:26px;width:380px}
.step{display:flex;gap:12px}
.step .ic{width:28px;height:28px;border-radius:6px;background:#1e2a4a;flex:none;display:flex;align-items:center;justify-content:center}
.step h4{font-family:"Oswald",sans-serif;font-weight:600;font-size:11px}
.step p{font-size:8.5px;color:var(--muted);margin-top:4px;line-height:1.4}
.creator .btn{margin-top:30px;height:34px;width:164px;justify-content:center;border-radius:4px}
.creator .media{height:381px;background:var(--white);border-radius:8px;overflow:hidden;box-shadow:0 0 60px rgba(224,38,43,.18)}
.app-bar{height:24px;background:#1c1d22;display:flex;align-items:center;padding:0 12px;gap:16px;font-size:7px;color:#d4d4d8}
.app-bar .go{margin-left:auto;background:var(--red);color:#fff;padding:3px 10px;border-radius:3px}
.app-stage{position:absolute;top:70px;left:20px;right:20px;height:250px;display:flex;gap:30px;justify-content:center;align-items:center}
.garment{width:150px;height:200px;border-radius:14px}
.garment.tee{background:linear-gradient(#20242e,#0f1117)}
.garment.hood{background:linear-gradient(#a8262c,#6c1418)}
.app-foot{position:absolute;bottom:10px;left:12px;right:12px;display:flex;justify-content:space-between;align-items:center}
.app-foot b{height:10px;width:60px;border-radius:3px;background:#f2a0a2}
.app-foot i{height:12px;width:40px;border-radius:3px;background:var(--red)}

.shop{height:1140px;background:var(--white);color:var(--text);text-align:center;padding-top:68px}
.shop h2{font-size:34px;margin-top:10px}
.shop h2 em{font-style:normal;color:var(--navy)}
.shop .lead{font-size:11px;color:var(--muted-dark);margin-top:12px}
.hero-gear{width:563px;height:560px;margin:34px auto 0;background:radial-gradient(circle at 50% 55%,#5a3a30,#c5602e 35%,#f5f5f5 70%);border-radius:8px;box-shadow:0 4px 20px rgba(0,0,0,.08)}
.products{display:flex;gap:14.6px;margin-top:42px;text-align:left}
.product{width:191px;height:220px;border:1px solid var(--line);border-radius:6px;padding:8px 16px;box-shadow:0 2px 10px rgba(0,0,0,.04)}
.product .badge{font-size:7px;color:var(--red);background:#fde8e8;padding:2px 6px;border-radius:10px;display:inline-block}
.product .thumb{height:100px;background:#f1f2f4;border-radius:4px;margin-top:6px;display:flex;align-items:center;justify-content:center}
.product .thumb span{width:20px;height:20px;border-radius:50%}
.product .cat{font-size:7px;color:var(--muted);text-transform:uppercase;margin-top:12px;letter-spacing:.4px}
.product h4{font-family:"Oswald",sans-serif;font-weight:600;font-size:10.5px;margin-top:4px;text-transform:uppercase}
.product .price{color:var(--red);font-weight:700;font-size:11.5px;margin-top:14px}
.product.plain{padding-top:14px}
.product.plain .thumb{margin-top:0}
.shop .btn{margin-top:30px;height:26px;font-size:9.5px}

.brands{height:130px;background:var(--light);color:var(--text);text-align:center;padding-top:34px}
.brands h3{font-family:"Oswald",sans-serif;font-weight:600;font-size:15px}
.brand-row{display:flex;justify-content:center;gap:40px;margin-top:26px;font-family:"Oswald",sans-serif;font-weight:500;font-size:15px;color:#a8adb8;text-transform:uppercase;letter-spacing:.6px}

.why{height:504px;background:var(--white);color:var(--text)}
.why h2 em{font-style:normal;color:var(--navy)}
.why .media{background:linear-gradient(160deg,#8a5a3a,#3a2a22 50%,#111)}
.feats{display:grid;grid-template-columns:1fr 1fr;gap:22px 24px;margin-top:26px;width:380px}
.feat{display:flex;gap:12px}
.feat .ic{width:28px;height:28px;border-radius:6px;background:#fde8e8;flex:none;display:flex;align-items:center;justify-content:center}
.feat h4{font-family:"Oswald",sans-serif;font-weight:600;font-size:11px}
.feat p{font-size:8.5px;color:var(--muted-dark);margin-top:4px;line-height:1.4}

.cta{height:270px;text-align:center;padding-top:56px;background:linear-gradient(90deg,#6a1a22,#3a2040 50%,#1e3478)}
.cta h2{font-size:30px}
.cta p{font-size:11.5px;color:#e4e4e7;width:410px;margin:12px auto 0;line-height:1.5}
.cta .actions{display:flex;justify-content:center;gap:14px;margin-top:22px}
.cta .btn{height:34px;width:146px;justify-content:center}
.cta .btn.outline{background:rgba(0,0,0,.25);border:1px solid rgba(255,255,255,.5);width:182px}

.footer{height:366px;background:var(--ink);padding-top:62px}
.foot-top{display:flex}
.foot-brand{width:335px}
.foot-brand p{font-size:9.5px;color:#c4c4cc;line-height:1.5;margin-top:12px;width:240px}
.contact{list-style:none;margin-top:14px;font-size:9.5px;color:#d4d4d8}
.contact li{display:flex;align-items:center;gap:9px;margin-bottom:9px}
.foot-col{width:167px}
.foot-col h5{font-family:"Oswald",sans-serif;font-weight:600;font-size:10px;text-transform:uppercase}
.foot-col ul{list-style:none;margin-top:14px;font-size:9.5px;color:#a1a1aa}
.foot-col li{margin-bottom:9px}
.foot-bottom{display:flex;justify-content:space-between;margin-top:42px;padding-top:14px;border-top:1px solid #26262a;font-size:8.5px;color:#8a8a92}
.foot-bottom nav{display:flex;gap:18px}
</style>
</head>
<body>

<header class="nav">
  <div class="wrap">
    <div class="brand"><i></i>Wren Sporting Goods</div>
    <ul><li>Shop</li><li>Custom Uniforms</li><li>Shirt Creator</li><li>About</li><li>Contact</li></ul>
    <svg class="cart" width="12" height="12" viewBox="0 0 24 24" fill="none" stroke="#fff" stroke-width="2"><path d="M3 4h3l2 11h11l2-8H7"/><circle cx="9" cy="20" r="1.5"/><circle cx="18" cy="20" r="1.5"/></svg>
    <span class="btn">Get a Quote</span>
  </div>
</header>

<section class="hero">
  <div class="hero-player left" role="img" aria-label="Basketball player in red team jersey"></div>
  <div class="hero-player right" role="img" aria-label="Basketball player in white team jersey"></div>
  <div class="hero-inner">
    <span class="tag">Team Sports Specialists</span>
    <h1 class="display">Gear Up. Stand Out.<span>Play to Win.</span></h1>
    <p>Custom uniforms, team apparel, and premium sporting goods for champions at every level.</p>
    <div class="actions">
      <span class="btn">✎ Design Your Uniform</span>
      <span class="btn blue">⛉ Shop Team Gear</span>
    </div>
    <div class="stats">
      <span><svg width="12" height="12" viewBox="0 0 24 24" fill="#eab308"><path d="M6 3h12v4a6 6 0 0 1-12 0zM10 15h4v3h3v3H7v-3h3z"/></svg>1000+ Teams Outfitted</span>
      <span><svg width="12" height="12" viewBox="0 0 24 24" fill="#eab308"><path d="M13 2 4 14h7l-1 8 9-12h-7z"/></svg>Fast Turnaround</span>
      <span><svg width="12" height="12" viewBox="0 0 24 24" fill="none" stroke="#d4d4d8" stroke-width="2.5"><path d="m5 12 5 5 9-10"/></svg>Premium Quality</span>
    </div>
  </div>
</section>

<section class="built">
  <div class="wrap">
    <h2 class="display">Built for <em>Your Game</em></h2>
    <p>Basketball, Football, and Baseball-focused gear, apparel, and team solutions.</p>
    <div class="sports">
      <div class="sport"><div class="ball" style="background:radial-gradient(circle at 35% 35%,#f08a3c,#c2521a)"></div><h3>BASKETBALL</h3><p>Jerseys, shorts, warm-ups, and court gear</p></div>
      <div class="sport"><div class="ball" style="background:radial-gradient(circle at 35% 35%,#b0643a,#6e3518);border-radius:50%/40%"></div><h3>FOOTBALL</h3><p>Helmets, pads, jerseys, and training equipment</p></div>
      <div class="sport"><div class="ball" style="background:radial-gradient(circle at 35% 35%,#ffffff,#cfcfcf)"></div><h3>BASEBALL</h3><p>Uniforms, gloves, bats, and field accessories</p></div>
    </div>
  </div>
</section>

<section class="uniforms">
  <div class="wrap split">
    <div class="media photo" role="img" aria-label="Team of athletes wearing custom red, white and blue uniforms"><span class="cap">Custom Built</span></div>
    <div class="copy">
      <span class="tag">Custom Uniforms</span>
      <h2 class="display">Custom Uniforms That<span>Define Your Team</span></h2>
      <p>From youth leagues to elite programs, Wren Sporting Goods delivers fully customized uniforms designed to represent your team's identity.</p>
      <ul class="checks">
        <li><svg width="11" height="11" viewBox="0 0 24 24"><circle cx="12" cy="12" r="11" fill="#fde8e8"/><path d="m7 12 3 3 7-7" stroke="#e0262b" stroke-width="2.5" fill="none"/></svg>Full sublimation printing</li>
        <li><svg width="11" height="11" viewBox="0 0 24 24"><circle cx="12" cy="12" r="11" fill="#fde8e8"/><path d="m7 12 3 3 7-7" stroke="#e0262b" stroke-width="2.5" fill="none"/></svg>Custom team colors &amp; logos</li>
        <li><svg width="11" height="11" viewBox="0 0 24 24"><circle cx="12" cy="12" r="11" fill="#fde8e8"/><path d="m7 12 3 3 7-7" stroke="#e0262b" stroke-width="2.5" fill="none"/></svg>Youth to adult sizing</li>
        <li><svg width="11" height="11" viewBox="0 0 24 24"><circle cx="12" cy="12" r="11" fill="#fde8e8"/><path d="m7 12 3 3 7-7" stroke="#e0262b" stroke-width="2.5" fill="none"/></svg>Fast 2-3 week turnaround</li>
        <li><svg width="11" height="11" viewBox="0 0 24 24"><circle cx="12" cy="12" r="11" fill="#fde8e8"/><path d="m7 12 3 3 7-7" stroke="#e0262b" stroke-width="2.5" fill="none"/></svg>No minimum order quantity</li>
        <li><svg width="11" height="11" viewBox="0 0 24 24"><circle cx="12" cy="12" r="11" fill="#fde8e8"/><path d="m7 12 3 3 7-7" stroke="#e0262b" stroke-width="2.5" fill="none"/></svg>Free design consultation</li>
      </ul>
      <div class="actions"><span class="btn">Start Designing</span><span class="btn ghost">View Catalog</span></div>
    </div>
  </div>
</section>

<section class="creator">
  <div class="wrap split">
    <div class="copy">
      <span class="tag blue">Online Tool</span>
      <h2 class="display">Create Custom Shirts <em>in<br>Minutes</em></h2>
      <p>Online apparel customization tool for teams, schools, and events. Design your perfect look with our easy-to-use creator.</p>
      <div class="steps">
        <div class="step"><div class="ic"><svg width="13" height="13" viewBox="0 0 24 24" fill="none" stroke="#60a5fa" stroke-width="2"><path d="M8 3 3 6l2 5 2-1v11h10V10l2 1 2-5-5-3a4 4 0 0 1-8 0z"/></svg></div><div><h4>1. Choose Style</h4><p>Pick from t-shirts, hoodies, polos &amp; more</p></div></div>
        <div class="step"><div class="ic"><svg width="13" height="13" viewBox="0 0 24 24" fill="none" stroke="#60a5fa" stroke-width="2"><circle cx="12" cy="12" r="9"/><circle cx="8" cy="10" r="1"/><circle cx="12" cy="7" r="1"/><circle cx="16" cy="10" r="1"/></svg></div><div><h4>2. Select Colors</h4><p>Match your team or brand colors</p></div></div>
        <div class="step"><div class="ic"><svg width="13" height="13" viewBox="0 0 24 24" fill="none" stroke="#60a5fa" stroke-width="2"><path d="M12 16V4m-5 5 5-5 5 5M4 16v4h16v-4"/></svg></div><div><h4>3. Add Your Logo</h4><p>Upload artwork or let us design</p></div></div>
        <div class="step"><div class="ic"><svg width="13" height="13" viewBox="0 0 24 24" fill="none" stroke="#60a5fa" stroke-width="2"><path d="M2 6h12v10H2zM14 10h4l3 3v3h-7"/><circle cx="6" cy="18" r="2"/><circle cx="17" cy="18" r="2"/></svg></div><div><h4>4. Fast Delivery</h4><p>Production &amp; shipping in 7-10 days</p></div></div>
      </div>
      <span class="btn blue">Launch Shirt Creator</span>
    </div>
    <div class="media">
      <div class="app-bar"><span>Custom shirt</span><span>Hoodie</span><span>Coverall</span><span style="margin-left:40px">Design</span><span>Mockup</span><span class="go">Get Quote</span></div>
      <div class="app-stage">
        <div class="garment tee" role="img" aria-label="Black t-shirt mockup with team crest"></div>
        <div class="garment hood" role="img" aria-label="Red hoodie mockup with team crest"></div>
      </div>
      <div class="app-foot"><b></b><i></i></div>
    </div>
  </div>
</section>

<section class="shop">
  <div class="wrap">
    <span class="tag">Shop Now</span>
    <h2 class="display">Shop Top <em>Team Gear</em></h2>
    <p class="lead">Premium equipment and apparel curated for team sports.</p>
    <div class="hero-gear" role="img" aria-label="Basketballs, football helmet, baseball glove and bat arranged together"></div>
    <div class="products">
      <div class="product"><span class="badge">Best Seller</span><div class="thumb"><span style="background:#d9622a"></span></div><div class="cat">Basketball</div><h4>Pro Basketball</h4><div class="price">$49.99</div></div>
      <div class="product"><span class="badge">New</span><div class="thumb"><span style="background:#8a4a22;border-radius:50%/38%"></span></div><div class="cat">Football</div><h4>Football Helmet Pro</h4><div class="price">$189.99</div></div>
      <div class="product plain"><div class="thumb"><span style="background:#ddd;border:2px solid #c33"></span></div><div class="cat">Baseball</div><h4>Leather Baseball Glove</h4><div class="price">$129.99</div></div>
      <div class="product"><span class="badge">Team Favorite</span><div class="thumb"><span style="background:#3b82f6;border-radius:4px"></span></div><div class="cat">Apparel</div><h4>Training Jersey Set</h4><div class="price">$79.99</div></div>
    </div>
    <span class="btn">View All Products</span>
  </div>
</section>

<section class="brands">
  <h3>BRANDS WE CARRY</h3>
  <div class="brand-row"><span>Korvel</span><span>Vantrel</span><span>Ironweave</span><span>Marlow</span><span>Hartline</span><span>Pellam</span></div>
</section>

<section class="why">
  <div class="wrap split">
    <div class="copy">
      <span class="tag">Why Choose Us</span>
      <h2 class="display">Why Teams Choose <em>Wren</em></h2>
      <p>Expertise, customization, and reliable service that makes us the go-to partner for teams across the country.</p>
      <div class="feats">
        <div class="feat"><div class="ic"><svg width="13" height="13" viewBox="0 0 24 24" fill="none" stroke="#e0262b" stroke-width="2"><circle cx="9" cy="8" r="3"/><path d="M3 20a6 6 0 0 1 12 0M16 5a3 3 0 0 1 0 6M18 20a6 6 0 0 0-2-5"/></svg></div><div><h4>Team Experts</h4><p>Decades of experience outfitting teams at every level</p></div></div>
        <div class="feat"><div class="ic"><svg width="13" height="13" viewBox="0 0 24 24" fill="none" stroke="#e0262b" stroke-width="2"><circle cx="12" cy="9" r="6"/><path d="m9 14-2 8 5-3 5 3-2-8"/></svg></div><div><h4>Premium Quality</h4><p>Only the best materials and construction for lasting performance</p></div></div>
        <div class="feat"><div class="ic"><svg width="13" height="13" viewBox="0 0 24 24" fill="none" stroke="#e0262b" stroke-width="2"><circle cx="12" cy="12" r="9"/><path d="M12 7v5l3 2"/></svg></div><div><h4>Fast Turnaround</h4><p>Rush orders available when you need gear quickly</p></div></div>
        <div class="feat"><div class="ic"><svg width="13" height="13" viewBox="0 0 24 24" fill="none" stroke="#e0262b" stroke-width="2"><path d="M12 20s-8-5-8-11a4 4 0 0 1 8-1 4 4 0 0 1 8 1c0 6-8 11-8 11z"/></svg></div><div><h4>Dedicated Service</h4><p>Personal account managers for seamless ordering</p></div></div>
      </div>
    </div>
    <div class="media photo" role="img" aria-label="Basketball team huddled together in a gym"></div>
  </div>
</section>

<section class="cta" role="img" aria-label="Red and blue sports banner with athlete silhouettes">
  <h2 class="display">Ready to Build Your Team's Look?</h2>
  <p>Get started with a free consultation and see how Wren Sporting Goods can elevate your team's identity.</p>
  <div class="actions"><span class="btn">Get a Free Quote</span><span class="btn outline">Call Us: (555) 010-2288</span></div>
</section>

<footer class="footer">
  <div class="wrap">
    <div class="foot-top">
      <div class="foot-brand">
        <div class="brand"><i></i>Wren Sporting Goods</div>
        <p>Your trusted partner for team sports equipment, custom uniforms, and premium sporting goods since 1985.</p>
        <ul class="contact">
          <li><svg width="11" height="11" viewBox="0 0 24 24" fill="none" stroke="#e0262b" stroke-width="2"><path d="M12 22s7-7 7-12a7 7 0 0 0-14 0c0 5 7 12 7 12z"/><circle cx="12" cy="10" r="2.5"/></svg>48 Fieldhouse Rd, Brookvale, BV 20418</li>
          <li><svg width="11" height="11" viewBox="0 0 24 24" fill="none" stroke="#e0262b" stroke-width="2"><path d="M5 3h4l2 5-3 2a11 11 0 0 0 6 6l2-3 5 2v4a2 2 0 0 1-2 2A17 17 0 0 1 3 5a2 2 0 0 1 2-2z"/></svg>(555) 010-2288</li>
          <li><svg width="11" height="11" viewBox="0 0 24 24" fill="none" stroke="#e0262b" stroke-width="2"><path d="M3 5h18v14H3z"/><path d="m3 6 9 7 9-7"/></svg>info@wrensporting.com</li>
          <li><svg width="11" height="11" viewBox="0 0 24 24" fill="none" stroke="#e0262b" stroke-width="2"><circle cx="12" cy="12" r="9"/><path d="M12 7v5l3 2"/></svg>Mon-Fri: 9am-6pm, Sat: 10am-4pm</li>
        </ul>
      </div>
      <div class="foot-col"><h5>Shop</h5><ul><li>Basketball</li><li>Football</li><li>Baseball</li><li>Team Apparel</li><li>Accessories</li></ul></div>
      <div class="foot-col"><h5>Services</h5><ul><li>Custom Uniforms</li><li>Shirt Creator</li><li>Team Orders</li><li>Bulk Discounts</li><li>Rush Orders</li></ul></div>
      <div class="foot-col"><h5>Company</h5><ul><li>About Us</li><li>Contact</li><li>Careers</li><li>Blog</li><li>Partners</li></ul></div>
    </div>
    <div class="foot-bottom"><span>© 2025 Wren Sporting Goods. All rights reserved.</span><nav><span>Privacy Policy</span><span>Terms of Service</span><span>Returns</span></nav></div>
  </div>
</footer>

</body>
</html>
```